Looking for business card/letterhead/email signature

Take existing logo and create full design suite of collateral

Contact Information for Business Card

Use mock details that can be edited by us

Font styles to use
Sans Serif

```html
<!DOCTYPE html>
<html lang="en">
<head>
<meta charset="UTF-8">
<title>Harlow Digital – Business Card</title>
<link href="https://fonts.googleapis.com/css2?family=Lato:wght@400;700;900&display=swap" rel="stylesheet">
<style>
  :root {
    --stage: #1d1d1f;
    --brand-blue: #0b56a6;
    --brand-blue-deep: #083f80;
    --brand-pink: #e0235f;
    --paper: #ffffff;
    --paper-shade: #eeeeef;
    --ink: #3a3a3c;
    --ink-soft: #6b6b70;
    --dot-grey: #c9c9cc;
  }
  * { box-sizing: border-box; margin: 0; padding: 0; }
  html, body { width: 1200px; height: 896px; overflow: hidden; }
  body {
    background: var(--stage);
    font-family: "Lato", sans-serif;
    display: flex;
    align-items: center;
    justify-content: center;
    gap: 48px;
  }
  .card {
    width: 520px;
    height: 298px;
    border-radius: 18px;
    position: relative;
    overflow: hidden;
  }

  /* Front */
  .card-front {
    background: linear-gradient(160deg, var(--brand-blue) 0%, var(--brand-blue-deep) 100%);
    display: flex;
    align-items: center;
    justify-content: center;
  }
  .front-texture {
    position: absolute;
    inset: 0;
    background:
      radial-gradient(ellipse at 80% 20%, rgba(255,255,255,0.10), transparent 55%),
      radial-gradient(ellipse at 20% 85%, rgba(255,255,255,0.07), transparent 55%);
  }
  .wordmark {
    position: relative;
    display: flex;
    align-items: center;
    gap: 12px;
    font-family: "Lato", sans-serif;
    font-weight: 900;
    line-height: 1;
  }
  .wordmark-dot {
    width: 14px; height: 14px;
    border-radius: 50%;
    background: var(--brand-pink);
  }
  .card-front .wordmark { color: var(--paper); font-size: 42px; }

  /* Back */
  .card-back { background: linear-gradient(135deg, var(--paper) 55%, var(--paper-shade) 100%); }
  .corner-dot {
    position: absolute;
    top: -22px; right: 70px;
    width: 44px; height: 44px;
    border-radius: 50%;
    background: var(--brand-pink);
  }
  .back-texture {
    position: absolute;
    right: 0; bottom: 0;
    width: 240px; height: 170px;
    background: radial-gradient(ellipse at 100% 100%, var(--dot-grey), transparent 70%);
    opacity: 0.7;
  }
  .card-back .wordmark {
    position: absolute;
    left: 34px; bottom: 40px;
    color: var(--brand-blue);
    font-size: 36px;
  }
  .contact {
    position: absolute;
    top: 36px; right: 34px;
    text-align: right;
    color: var(--ink);
    font-size: 12.5px;
    line-height: 1.45;
  }
  .contact-name { color: var(--brand-blue); font-weight: 700; font-size: 20px; line-height: 1.2; }
  .contact-title { color: var(--ink-soft); font-size: 12px; margin-bottom: 10px; }
  .contact-company { color: var(--brand-blue); font-weight: 700; font-size: 13px; }
  .contact-address { margin-bottom: 12px; }
  .contact-line { display: flex; justify-content: flex-end; align-items: center; gap: 8px; }
  .contact-line svg { width: 12px; height: 12px; fill: var(--brand-blue); flex: none; }
</style>
</head>
<body>
  <section class="card card-front">
    <div class="front-texture" role="img" aria-label="Subtle dotted halftone texture on blue"></div>
    <div class="wordmark"><span class="wordmark-dot"></span>harlow digital</div>
  </section>

  <section class="card card-back">
    <div class="corner-dot"></div>
    <div class="back-texture" role="img" aria-label="Grey dotted halftone texture"></div>

    <div class="contact">
      <div class="contact-name">Marcus Tembe</div>
      <div class="contact-title">Chief Executive Officer</div>
      <div class="contact-company">Harlow Digital</div>
      <div class="contact-address">480 Harbor View Ave.<br>Seaside Bay FL 00000</div>
      <div class="contact-line">(555) 210-4471
        <svg viewBox="0 0 24 24"><path d="M6.6 10.8a15 15 0 0 0 6.6 6.6l2.2-2.2a1 1 0 0 1 1-.25 11.4 11.4 0 0 0 3.6.57 1 1 0 0 1 1 1V20a1 1 0 0 1-1 1A17 17 0 0 1 3 4a1 1 0 0 1 1-1h3.5a1 1 0 0 1 1 1c0 1.25.2 2.45.57 3.57a1 1 0 0 1-.25 1z"/></svg>
      </div>
      <div class="contact-line">(555) 210-4472
        <svg viewBox="0 0 24 24"><path d="M6 2h12v5H6zM4 8h16a2 2 0 0 1 2 2v7h-4v5H6v-5H2v-7a2 2 0 0 1 2-2zm4 8v4h8v-4z"/></svg>
      </div>
      <div class="contact-line">info@HarlowDigital.com
        <svg viewBox="0 0 24 24"><path d="M2 5h20v14H2zm2 2v.5l8 5 8-5V7z"/></svg>
      </div>
      <div class="contact-line">www.HarlowDigital.com
        <svg viewBox="0 0 24 24"><circle cx="12" cy="12" r="9.5" fill="none" stroke="#0b56a6" stroke-width="2"/><path d="M2.5 12h19M12 2.5c3 3 3 16 0 19M12 2.5c-3 3-3 16 0 19" fill="none" stroke="#0b56a6" stroke-width="1.6"/></svg>
      </div>
    </div>

    <div class="wordmark"><span class="wordmark-dot"></span>harlow digital</div>
  </section>
</body>
</html>
```